KINDLED Print Shop

We need postcards for a new print shop in Newark Delaware called KINDLED. We specialize in screen printing however the fun doesn't stop there...we also provide services for many other promotional product such as; embroidery, decals/ stickers, banners, yard signs, and sublimation products. We deal with customers from all walks of life; businesses, sporting events, bands, bars/restaurants, schools/ colleges. Our main goal is to have our customers look awesome in that custom shirt, hat, or any other custom product that we make because let’s face it first impressions are everything! At KINDLED we strive to create a lasting experience every step of the way to ensure complete satisfaction and trust in our products. The colors we use to identify ourselves are neon green and turquoise. The slogan we want to run with is, "we bring your ideas to life". On the back we would like to add a 10% off next order coupon to generate new revenue.
Color Breakdown in logo:
Green- R=0, G=255, B=0
blue- R=0, G=118, B=163
Updates
Reason: times running out we still need a design!!
Target Market(s)
everybody & anybody
Industry/Entity Type
Promotional Product
Requirements
Must have
- website: www.kindledscreenworks.example
contact info: (555)214-7093 & kindledsw@mailbox.example
like us on FB: www.social.example/kindledprintshop
Nice to have
- stack of t-shirts

```html
<!DOCTYPE html>
<html lang="en">
<head>
<meta charset="utf-8">
<title>KINDLED Print Shop – Postcard</title>
<link rel="stylesheet" href="https://fonts.googleapis.com/css2?family=Archivo+Black&family=Roboto+Condensed:wght@400;700&display=swap">
<style>
  :root {
    --turquoise: #1b8ec2;
    --turquoise-light: #2c9dd2;
    --green: #5ab947;
    --green-lime: #b6d75a;
    --white: #ffffff;
    --ink-blue: #1e7fb8;
    --logo-ink: #0e4f6b;
    --yellow: #f3e23a;
    --stamp: #e6e6e6;
    --rule: #d9d9d9;
    --tile-blue: #8fd0ef;
    --tile-peach: #e7b48f;
  }
  * { margin: 0; padding: 0; box-sizing: border-box; }
  html, body { width: 775px; height: 1200px; overflow: hidden; background: var(--white); }
  .postcard {
    position: relative; width: 775px; height: 1200px; overflow: hidden;
    font-family: "Roboto Condensed", Arial, sans-serif; color: var(--white);
  }
  .abs { position: absolute; }

  /* Front hero */
  .hero { left: 0; top: 0; width: 775px; height: 460px; background: var(--turquoise); }
  .hero-corner { left: 0; top: 0; }
  .brand-mark {
    left: 29px; top: 22px; font-family: "Archivo Black", Arial, sans-serif;
    font-size: 44px; color: var(--logo-ink); letter-spacing: 1px;
  }
  .hero-photo {
    left: 110px; top: 108px; width: 410px; height: 352px;
    background: linear-gradient(160deg, #3b4a55 0%, #23282d 55%, #5c6670 100%);
    border-radius: 4px 4px 0 0; opacity: .9;
  }
  .slogan {
    left: 385px; top: 62px; width: 380px; text-align: center;
    font-family: "Archivo Black", Arial, sans-serif; font-size: 42px; line-height: 58px;
    text-transform: uppercase; text-shadow: 2px 2px 3px rgba(0,0,0,.35); white-space: nowrap;
  }

  /* Bars */
  .contact-bar { left: 0; top: 460px; width: 775px; height: 47px; background: var(--green); }
  .contact-bar .item, .footer-bar .item {
    position: absolute; display: flex; align-items: center; gap: 14px;
    font-weight: 700; font-size: 22px; white-space: nowrap;
  }
  .coupon-strip {
    left: 0; top: 507px; width: 775px; height: 44px; background: var(--white);
    color: var(--ink-blue); font-size: 21px; line-height: 44px; padding-left: 29px;
    text-transform: uppercase; letter-spacing: .2px;
  }
  .coupon-badge {
    left: 675px; top: 502px; width: 58px; height: 58px; border-radius: 50%;
    background: var(--green); border: 3px solid var(--white);
  }
  .web-bar {
    left: 0; top: 551px; width: 775px; height: 36px; background: var(--green);
    font-size: 15px; line-height: 36px;
  }
  .web-bar .site { position: absolute; left: 29px; }
  .web-bar .social { position: absolute; right: 33px; }

  /* Back: services panel */
  .services { left: 0; top: 587px; width: 375px; height: 506px; background: var(--turquoise-light); }
  .tile {
    position: absolute; display: flex; align-items: center; justify-content: center;
    text-align: center; text-transform: uppercase; font-size: 14px; line-height: 16px;
    color: var(--white); box-shadow: 1px 2px 4px rgba(0,0,0,.25);
  }
  .tile--product { left: 87px; top: 50px; width: 66px; height: 63px; background: var(--tile-blue); transform: rotate(-10deg); }
  .tile--eagle { left: 153px; top: 33px; width: 62px; height: 60px; background: var(--white); }
  .tile--shirt { left: 216px; top: 43px; width: 80px; height: 62px; background: var(--green-lime); transform: rotate(8deg); }
  .tile--signs { left: 55px; top: 120px; width: 87px; height: 62px; background: var(--green); transform: rotate(-10deg); }
  .tile--badge { left: 167px; top: 107px; width: 56px; height: 56px; border-radius: 50%; background: var(--green); border: 3px solid var(--white); }
  .tile--flower { left: 234px; top: 100px; width: 62px; height: 70px; background: #f6ecec; transform: rotate(8deg); }
  .tile--banners { left: 173px; top: 166px; width: 100px; height: 72px; background: var(--tile-peach); transform: rotate(-10deg); }
  .tile--mug { left: 104px; top: 157px; width: 80px; height: 80px; background: #f2f2f2; transform: rotate(-10deg); }

  .services-heading {
    position: absolute; left: 29px; top: 264px; width: 340px;
    font-family: "Roboto Condensed", Arial, sans-serif; font-weight: 700;
    font-size: 22px; line-height: 31px; white-space: nowrap;
    color: var(--yellow); text-transform: uppercase;
  }
  .audience { position: absolute; top: 341px; list-style: none; }
  .audience li {
    display: flex; align-items: center; gap: 9px; height: 23px;
    font-weight: 700; font-size: 14px; text-transform: uppercase;
  }
  .audience--left { left: 49px; }
  .audience--right { left: 199px; }
  .services-brand {
    position: absolute; left: 0; width: 375px; top: 460px; text-align: center;
    font-family: "Archivo Black", Arial, sans-serif; font-size: 30px; color: var(--white);
  }

  /* Back: address side */
  .stamp-box { left: 583px; top: 620px; width: 126px; height: 173px; background: var(--stamp); }
  .address-line { left: 387px; width: 354px; height: 3px; background: var(--rule); }

  .footer-bar { left: 0; top: 1093px; width: 775px; height: 107px; background: var(--green); }
</style>
</head>
<body>
<div class="postcard">

  <section class="hero abs">
    <svg class="hero-corner abs" width="775" height="460" viewBox="0 0 775 460" aria-hidden="true">
      <polygon points="0,0 385,0 0,232" fill="#ffffff"/>
      <polygon points="385,0 408,0 0,246 0,232" fill="#5ab947"/>
    </svg>
    <div class="hero-photo abs" role="img" aria-label="Three young men wearing hats and custom printed clothing"></div>
    <div class="brand-mark abs">KINDLED</div>
    <h1 class="slogan abs">“ We bring<br>your<br>ideas to<br>life ”</h1>
  </section>

  <div class="contact-bar abs">
    <div class="item" style="left:29px;top:8px;">
      <svg width="38" height="32" viewBox="0 0 38 32" aria-hidden="true">
        <ellipse cx="19" cy="16" rx="17" ry="14" fill="none" stroke="#fff" stroke-width="2.5"/>
        <path d="M13 9c-2 2-1 6 3 10s8 5 10 3l-3-3-2 1c-2-1-4-3-5-5l1-2z" fill="#fff"/>
      </svg>
      <span>(555)214-7093</span>
    </div>
    <div class="item" style="right:33px;top:8px;">
      <svg width="46" height="30" viewBox="0 0 46 30" aria-hidden="true">
        <rect x="1" y="1" width="44" height="28" fill="#fff"/>
        <path d="M2 2l21 15L44 2M2 28l15-13M44 28L29 15" fill="none" stroke="#5ab947" stroke-width="2"/>
      </svg>
      <span>kindledsw@mailbox.example</span>
    </div>
  </div>

  <div class="coupon-strip abs">10% off next order coupon to generate new revenue</div>
  <div class="coupon-badge abs" aria-hidden="true"></div>

  <div class="web-bar abs">
    <span class="site">www.kindledscreenworks.example</span>
    <span class="social">www.social.example/kindledprintshop</span>
  </div>

  <section class="services abs">
    <div class="tile tile--product">Custom<br>product</div>
    <div class="tile tile--eagle" role="img" aria-label="Eagle print design"></div>
    <div class="tile tile--shirt">Custom<br>shirt</div>
    <div class="tile tile--signs">Yard signs</div>
    <div class="tile tile--flower" role="img" aria-label="Floral print design"></div>
    <div class="tile tile--mug" role="img" aria-label="Custom printed mug"></div>
    <div class="tile tile--banners">Banners</div>
    <div class="tile tile--badge" aria-hidden="true"></div>

    <h2 class="services-heading">Specialize in screen printing<br>&amp; promotion products ...</h2>

    <ul class="audience audience--left">
      <li><svg width="16" height="14" viewBox="0 0 16 14" aria-hidden="true"><path d="M1 8l5 5L15 1" fill="none" stroke="#fff" stroke-width="3"/></svg>Life</li>
      <li><svg width="16" height="14" viewBox="0 0 16 14" aria-hidden="true"><path d="M1 8l5 5L15 1" fill="none" stroke="#fff" stroke-width="3"/></svg>Sporting</li>
      <li><svg width="16" height="14" viewBox="0 0 16 14" aria-hidden="true"><path d="M1 8l5 5L15 1" fill="none" stroke="#fff" stroke-width="3"/></svg>Bands</li>
      <li><svg width="16" height="14" viewBox="0 0 16 14" aria-hidden="true"><path d="M1 8l5 5L15 1" fill="none" stroke="#fff" stroke-width="3"/></svg>Restaurants</li>
      <li><svg width="16" height="14" viewBox="0 0 16 14" aria-hidden="true"><path d="M1 8l5 5L15 1" fill="none" stroke="#fff" stroke-width="3"/></svg>Colleges</li>
    </ul>
    <ul class="audience audience--right">
      <li><svg width="16" height="14" viewBox="0 0 16 14" aria-hidden="true"><path d="M1 8l5 5L15 1" fill="none" stroke="#fff" stroke-width="3"/></svg>Businesses</li>
      <li><svg width="16" height="14" viewBox="0 0 16 14" aria-hidden="true"><path d="M1 8l5 5L15 1" fill="none" stroke="#fff" stroke-width="3"/></svg>Events</li>
      <li><svg width="16" height="14" viewBox="0 0 16 14" aria-hidden="true"><path d="M1 8l5 5L15 1" fill="none" stroke="#fff" stroke-width="3"/></svg>Bars</li>
      <li><svg width="16" height="14" viewBox="0 0 16 14" aria-hidden="true"><path d="M1 8l5 5L15 1" fill="none" stroke="#fff" stroke-width="3"/></svg>Schools</li>
    </ul>

    <div class="services-brand">KINDLED</div>
  </section>

  <div class="stamp-box abs" aria-label="Stamp area"></div>
  <div class="address-line abs" style="top:873px;"></div>
  <div class="address-line abs" style="top:920px;"></div>
  <div class="address-line abs" style="top:967px;"></div>
  <div class="address-line abs" style="top:1013px;"></div>
  <div class="address-line abs" style="top:1060px;"></div>

  <footer class="footer-bar abs">
    <div class="item" style="left:24px;top:12px;">
      <svg width="38" height="32" viewBox="0 0 38 32" aria-hidden="true">
        <ellipse cx="19" cy="16" rx="17" ry="14" fill="none" stroke="#fff" stroke-width="2.5"/>
        <path d="M13 9c-2 2-1 6 3 10s8 5 10 3l-3-3-2 1c-2-1-4-3-5-5l1-2z" fill="#fff"/>
      </svg>
      <span>(555)214-7093</span>
    </div>
    <div class="item" style="left:22px;top:56px;">
      <svg width="46" height="30" viewBox="0 0 46 30" aria-hidden="true">
        <rect x="1" y="1" width="44" height="28" fill="#fff"/>
        <path d="M2 2l21 15L44 2M2 28l15-13M44 28L29 15" fill="none" stroke="#5ab947" stroke-width="2"/>
      </svg>
      <span>kindledsw@mailbox.example</span>
    </div>
  </footer>

</div>
</body>
</html>
```